Business Card Design

Copperfield Lantern Works, Inc. (CLW), located in Memphis, TN began operating on 2003. We are a certified
minority woman-owned business that genuinely takes a vested interest in our customers. We serve utilities,
government, contractors and end user markets in electrical, water, gas and industrial supplies. Our core
competency as a distributor of electrical materials has positioned us to serve business of all size. As your supply
chain partner, we arm you with the resources you need to make your supply chain more efficient. Our team
works with your team on a daily basis to help you solve problems and achieve goals. This team approach has
helped CLW customers to succeed and we can do the same for you.

NAICS Codes:
423610 Electrical Apparatus and Equipment, Wiring Supplies, and Related Equipment Merchant
Wholesalers
423510 Metal Service Centers and Other Metal Merchant Wholesalers
423720 Plumbing and Heating Equipment and Supplies (Hydronics) Merchant Wholesalers

Certifications
MBE (KRVPQAL, State of Tennessee Up-RFX and HJW), WBE (QOZRT),
WOSB, DOT (TDOT, MDOT, ALDOT, SCDOT, NCDOT, and VDOT), LOSB,
SBE, and LSB Certified
Some of Our Products Include:
. Boxes & Covers
. Conduit & Raceway
. Fittings
. Fuses
. Lamp & Ballasts
. Lighting Controls & Timers
. Lighting Fixtures
. Personal Safety
. Pipes
. Power Distribution
. Terminations Ground & Splices
. Tools & Testers
. Wire, Cords & Cable
. Wiring Devices
. Valves

Industry/Entity Type

Business

Contact Information for Business Card

Harriet M. Pendlow - President/CEO
4817 Galvin Ave., Memphis, TN 38127
901-482-6317 office, 901-482-6319 fax, 901-358-2074 cell
hmpendlow@clwgroupx.com - www.clwworksx.com

```html
<!DOCTYPE html>
<html lang="en">
<head>
<meta charset="UTF-8">
<title>Copperfield Lantern Works — Business Card</title>
<link rel="stylesheet" href="https://fonts.googleapis.com/css2?family=Open+Sans:wght@400;600&display=swap">
<style>
  :root {
    --backdrop: #e8e5e1;
    --card-white: #ffffff;
    --card-black: #000000;
    --olive: #9b9a14;
    --gold: #b5b01c;
    --gold-light: #dcd52e;
    --icon-yellow: #e3d62a;
    --ink: #111111;
    --text-light: #ffffff;
  }
  * { margin: 0; padding: 0; box-sizing: border-box; }
  html, body {
    width: 1200px; height: 900px; overflow: hidden;
    background: var(--backdrop);
    font-family: "Open Sans", Arial, sans-serif;
  }
  .business-card {
    position: absolute;
    left: 160px; top: 178px;
    width: 880px; height: 543px;
    background: var(--card-white);
    overflow: hidden;
    box-shadow: 0 6px 24px rgba(0,0,0,0.18);
  }
  .card-wave { position: absolute; inset: 0; width: 100%; height: 100%; }
  .holder { position: absolute; right: 40px; top: 30px; text-align: right; }
  .holder-name { color: var(--olive); font-weight: 600; font-size: 29px; line-height: 1.2; }
  .holder-title { color: var(--ink); font-size: 20px; line-height: 1.3; }
  .company-name {
    position: absolute; left: 54px; top: 186px;
    color: var(--ink); font-weight: 400;
    font-size: 33px; line-height: 1.12; letter-spacing: 0.5px;
    text-transform: uppercase;
  }
  .contact-list {
    position: absolute; right: 36px; top: 283px;
    list-style: none; text-align: right;
    color: var(--text-light); font-size: 21px;
  }
  .contact-list li {
    display: flex; justify-content: flex-end; align-items: center;
    height: 36.5px;
  }
  .contact-icon { width: 18px; height: 18px; margin-left: 16px; fill: var(--icon-yellow); }
  .contact-list .address { margin-top: 2px; }
</style>
</head>
<body>
  <div class="business-card">
    <svg class="card-wave" viewBox="0 0 652 402" preserveAspectRatio="none">
      <defs>
        <linearGradient id="gold-band" x1="0" y1="0" x2="1" y2="0">
          <stop offset="0" stop-color="#a3a012"/>
          <stop offset="0.5" stop-color="#e6df35"/>
          <stop offset="1" stop-color="#a9a414"/>
        </linearGradient>
      </defs>
      <path d="M0,204 C90,268 150,306 230,291 C330,271 420,140 520,111 C590,94 630,132 652,158 L652,402 L0,402 Z" fill="url(#gold-band)"/>
      <path d="M0,217 C90,282 150,322 230,307 C330,287 420,172 520,142 C580,126 620,150 652,176 L652,402 L0,402 Z" fill="var(--card-black)" stroke="var(--card-white)" stroke-width="4"/>
    </svg>

    <div class="holder">
      <p class="holder-name">Harriet M. Pendlow</p>
      <p class="holder-title">President/CEO</p>
    </div>

    <p class="company-name">Copperfield<br>Lantern Works</p>

    <ul class="contact-list">
      <li>901-482-6317
        <svg class="contact-icon" viewBox="0 0 24 24"><path d="M6.6 10.8a15.1 15.1 0 0 0 6.6 6.6l2.2-2.2c.3-.3.7-.4 1-.2 1.1.4 2.3.6 3.6.6.6 0 1 .4 1 1V20c0 .6-.4 1-1 1C10.6 21 3 13.4 3 4c0-.6.4-1 1-1h3.5c.6 0 1 .4 1 1 0 1.3.2 2.5.6 3.6.1.3 0 .7-.2 1z"/></svg>
      </li>
      <li>901-358-2074
        <svg class="contact-icon" viewBox="0 0 24 24"><path d="M7 2h10a2 2 0 0 1 2 2v16a2 2 0 0 1-2 2H7a2 2 0 0 1-2-2V4a2 2 0 0 1 2-2zm0 3v13h10V5zm5 14.2a1 1 0 1 0 0 .1z"/></svg>
      </li>
      <li>901-482-6319
        <svg class="contact-icon" viewBox="0 0 24 24"><path d="M8 3h9v5H8zM4 8h2v13H4a1 1 0 0 1-1-1V9a1 1 0 0 1 1-1zm4 6V9h12a1 1 0 0 1 1 1v10a1 1 0 0 1-1 1H8zm3-3v2h2v-2zm4 0v2h2v-2zm-4 4v2h2v-2zm4 0v2h2v-2z"/></svg>
      </li>
      <li>hmpendlow@clwgroupx.com
        <svg class="contact-icon" viewBox="0 0 24 24"><path d="M2 5h20v14H2zm2 2v.4l8 5.2 8-5.2V7zm0 2.8V17h16V9.8l-8 5.2z"/></svg>
      </li>
      <li>www.clwworksx.com
        <svg class="contact-icon" viewBox="0 0 24 24"><path d="M12 2a10 10 0 1 0 0 20 10 10 0 0 0 0-20zm-1 17.9A8 8 0 0 1 4.1 10L9 15v1a2 2 0 0 0 2 2zm6.9-2.5A2 2 0 0 0 16 16h-1v-3a1 1 0 0 0-1-1H8v-2h2a1 1 0 0 0 1-1V7h2a2 2 0 0 0 2-2v-.4a8 8 0 0 1 2.9 12.8z"/></svg>
      </li>
      <li class="address">4817 Galvin Ave., Memphis, TN 38127</li>
    </ul>
  </div>
</body>
</html>
```